Income Tax Business Cards - Updates

Need to update these business cards while keeping all the same wording but just update them and make them look nicer and more modern/ on brand with our brand.

Industry/Entity Type

finance

Contact Information for Business Card

we have multiple locations so will just need to easily be able to change the address and phone numbers

Colors

Designer to choose colors to be used in the design.

```html
<!DOCTYPE html>
<html lang="en">
<head>
<meta charset="UTF-8">
<title>Tax Service Business Card – Front and Back</title>
<link href="https://fonts.googleapis.com/css2?family=Montserrat:wght@500;600;700&family=Oswald:wght@600;700&family=Russo+One&display=swap" rel="stylesheet">
<style>
  :root {
    --canvas-bg: #e4e4e4;
    --card-white: #ffffff;
    --brand-green: #0e6a35;
    --brand-green-deep: #0b5a2c;
    --lime-light: #9be04a;
    --lime-dark: #2f8d1c;
    --brand-red: #c4242b;
    --ink: #1c1c1c;
    --photo-light: #f1efea;
    --photo-mid: #dcd6cc;
  }
  * { margin: 0; padding: 0; box-sizing: border-box; }
  html, body {
    width: 1200px; height: 1200px; overflow: hidden;
    background: var(--canvas-bg);
  }
  .sheet {
    width: 1200px; height: 1200px;
    display: flex; align-items: center; justify-content: center; gap: 40px;
  }
  .card {
    position: relative;
    width: 540px; height: 310px;
    overflow: hidden;
    background: var(--card-white);
    box-shadow: 0 2px 6px rgba(0,0,0,0.08);
  }

  /* Front */
  .card-front__photo {
    position: absolute; inset: 0;
    background: linear-gradient(135deg, var(--photo-light) 0%, var(--photo-mid) 55%, #ece8e1 100%);
  }
  .card-front__veil {
    position: absolute; inset: 0;
    background: rgba(255,255,255,0.55);
  }
  .headline {
    position: absolute; left: 0; right: 0; top: 30px;
    text-align: center;
    font-family: "Oswald", sans-serif; font-weight: 700;
    font-size: 39px; line-height: 1; letter-spacing: 0.2px;
    color: var(--brand-green);
    text-transform: uppercase;
  }
  .offer-pill {
    position: absolute; left: 82px; top: 91px;
    width: 376px; height: 58px;
    border-radius: 29px;
    background: var(--brand-red);
    display: flex; align-items: center; justify-content: center;
    font-family: "Oswald", sans-serif; font-weight: 700;
    font-size: 38px; color: #fff; text-transform: uppercase;
  }
  .amount {
    position: absolute; left: 0; right: 0; top: 166px;
    text-align: center;
    font-family: "Russo One", sans-serif;
    font-size: 50px; line-height: 1.1; letter-spacing: 1px;
    color: var(--lime-light);
    -webkit-text-stroke: 2px var(--lime-dark);
    text-shadow: 0 3px 0 var(--brand-green-deep), 0 5px 4px rgba(0,0,0,0.25);
  }
  .advance {
    position: absolute; left: 0; right: 0; top: 228px;
    text-align: center;
    font-family: "Montserrat", sans-serif; font-weight: 500;
    font-size: 27px; line-height: 1; letter-spacing: 0.5px;
    color: var(--brand-red); text-transform: uppercase;
  }
  .fine-print {
    position: absolute; left: 0; right: 0; top: 263px;
    text-align: center;
    font-family: "Montserrat", sans-serif; font-weight: 600;
    font-size: 15px; line-height: 1;
    color: var(--ink); text-transform: uppercase;
  }

  /* Back */
  .brand-name {
    position: absolute; left: 33px; top: 50px;
    font-family: "Montserrat", sans-serif; font-weight: 600;
    font-size: 30px; line-height: 1;
    color: var(--brand-green);
  }
  .phone-bar {
    position: absolute; left: 0; top: 138px;
    width: 308px; height: 50px;
    background: var(--brand-red);
    border-radius: 0 25px 25px 0;
    display: flex; align-items: center; gap: 10px;
    padding-left: 32px;
    font-family: "Oswald", sans-serif; font-weight: 600;
    font-size: 32px; color: #fff;
  }
  .phone-bar svg { width: 26px; height: 26px; flex: none; }
  .address {
    position: absolute; left: 33px; top: 222px;
    font-family: "Montserrat", sans-serif; font-weight: 500;
    font-size: 15.5px; line-height: 20px;
    font-style: normal;
    color: var(--ink);
  }
  .footer-band {
    position: absolute; left: 0; right: 0; bottom: 0;
    height: 21px;
    background: var(--brand-green);
  }
</style>
</head>
<body>
<main class="sheet">

  <section class="card card-front">
    <div class="card-front__photo" role="img" aria-label="Soft background photo of a smiling woman in a bright kitchen"></div>
    <div class="card-front__veil"></div>
    <h1 class="headline">File your taxes here</h1>
    <div class="offer-pill">Free estimates!</div>
    <p class="amount">UP TO $6,000</p>
    <p class="advance">Same day advance</p>
    <p class="fine-print">On approved tax returns!</p>
  </section>

  <section class="card card-back">
    <p class="brand-name">Ledgerline Financial Group</p>
    <div class="phone-bar">
      <svg viewBox="0 0 24 24" aria-hidden="true">
        <path fill="#fff" d="M6.6 10.8c1.4 2.8 3.8 5.1 6.6 6.6l2.2-2.2c.3-.3.7-.4 1-.2 1.1.4 2.3.6 3.6.6.6 0 1 .4 1 1V20c0 .6-.4 1-1 1C10.6 21 3 13.4 3 4c0-.6.4-1 1-1h3.5c.6 0 1 .4 1 1 0 1.3.2 2.5.6 3.6.1.3 0 .7-.2 1L6.6 10.8z"/>
      </svg>
      <span>(555)555-5555</span>
    </div>
    <address class="address">
      Address Line 1,<br>
      Address Line 2,<br>
      Address Line 3.
    </address>
    <div class="footer-band"></div>
  </section>

</main>
</body>
</html>
```